Energieberatung sucht Corporate Design
Zielgruppe
Ich führe Energieberatungen für Immobilieneigentümer durch, erstelle Sanierungsvorschläge sowie Förderanträge. Für Verkäufer und Vermieter fertige ich Energieausweise an, um die energetisch Qualität des Gebäudes darzustellen.
Energieberatung soll für die Kunden ein Wegweiser für modernes, klimaneutrales und kostengünstiges Wohnen sein.
Meine Zielgruppe sind Immobilieneigentümer, Verkäufer und Vermieter von Immobilien sowie Käufer von Immobilien.
Aufgabenstellung
Ich suche ein hochwertiges Design, welches modern und zeitlos ist, aber auch die energetische Komponente berücksichtigt. Mit dem Design soll das verstaubte Image der Energieberatung abgelegt werden. Die Kunden sollen damit zukunftsorientiertes, modernes Wohnen, Wohnqualität und Kostenersparnis verbinden.

```html
<!DOCTYPE html>
<html lang="de">
<head>
<meta charset="utf-8">
<title>Energieberatung Mira Wendel – Geschäftsausstattung</title>
<link href="https://fonts.googleapis.com/css2?family=Bree+Serif&display=swap" rel="stylesheet">
<style>
:root{
  --teal:#137b98;
  --teal-dark:#106f8c;
  --lime:#c3c20a;
  --yellow:#e2d200;
  --grey-text:#7c7c7c;
  --ink:#2b2b2b;
  --paper:#ffffff;
  --paper-grey:#e8e8e6;
  --stage:#b0b5bc;
  --shadow:0 4px 10px rgba(40,45,55,.35);
}
*{margin:0;padding:0;box-sizing:border-box}
html,body{width:999px;height:1200px;overflow:hidden}
body{background:var(--stage);font-family:"Bree Serif",Georgia,serif;position:relative}
.sheet{position:absolute;background:var(--paper);box-shadow:var(--shadow)}
.brand{position:absolute;display:flex;align-items:center;gap:.5em;color:var(--teal);line-height:1.1}
.brand .mark{width:.9em;height:.9em;background:var(--teal);flex:none}
.brand .name small{display:block;font-size:.72em;letter-spacing:.05em}
.contact{position:absolute;color:var(--teal);font-size:6.4px;line-height:9.8px;border-left:1px solid var(--lime);padding-left:9px}
.contact li{list-style:none;display:flex;align-items:center;gap:4px}
.contact svg{width:6px;height:6px;fill:none;stroke:var(--teal);stroke-width:1.2}
.small{font-size:6.4px;line-height:10px;color:var(--ink)}

/* envelope */
.envelope{left:363px;top:28px;width:582px;height:264px}
.envelope .brand{left:140px;top:110px;font-size:22px}

/* business card front */
.card-front{left:56px;top:341px;width:236px;height:152px}
.card-front .brand{left:16px;top:28px;font-size:11px}
.card-front .role{position:absolute;left:16px;top:76px;font-size:6.6px;color:var(--ink)}
.card-front .role b{color:var(--teal);font-weight:400}
.card-front .address{position:absolute;left:16px;top:117px}
.card-front .contact{left:118px;top:99px;border-color:var(--teal)}
.card-front .band{position:absolute;left:0;right:0;bottom:0;height:8px;background:var(--lime);clip-path:polygon(6px 0,calc(100% - 6px) 0,100% 100%,0 100%)}

/* business card back */
.card-back{left:56px;top:508px;width:236px;height:152px;background:var(--teal)}
.card-back .brand{color:var(--lime);left:50%;top:54px;transform:translateX(-50%);font-size:14px;white-space:nowrap}
.card-back .brand .mark{background:var(--lime)}
.card-back .url{position:absolute;left:0;right:0;top:108px;text-align:center;color:#fff;font-size:7px}

/* logo variants */
.card-grey{left:55px;top:697px;width:235px;height:152px;background:var(--paper-grey)}
.card-mono{left:55px;top:867px;width:235px;height:152px}
.card-grey .brand,.card-mono .brand{left:54px;top:60px;font-size:11px}
.card-mono .brand{color:#111}
.card-mono .brand .mark{background:#111}

/* letterhead */
.letterhead{left:363px;top:339px;width:581px;height:822px}
.letterhead .band-top{position:absolute;left:0;right:0;top:0;height:15px;background:linear-gradient(90deg,var(--teal),#7e9f70 50%,var(--yellow));clip-path:polygon(0 0,100% 0,calc(100% - 15px) 100%,15px 100%)}
.letterhead .brand{left:60px;top:62px;font-size:15px}
.letterhead .contact{left:446px;top:50px}
.letterhead .sender{position:absolute;left:60px;top:125px;font-size:6px;color:var(--teal)}
.footer{position:absolute;left:60px;right:20px;top:769px;display:flex}
.footer .col{font-size:6.2px;line-height:10.5px;color:var(--ink);padding:0 12px;border-left:1px solid var(--lime)}
.footer .col:first-child{padding-left:0;border-left:0}
.footer .col b{font-weight:400;color:var(--teal);display:block}
.footer .contact{position:static;border:0;padding:0;color:var(--ink);font-size:6.2px;line-height:10.5px}
.footer .contact svg{stroke:var(--ink)}
.letterhead .band-bottom{position:absolute;left:0;right:0;bottom:0;height:15px;background:var(--teal-dark);clip-path:polygon(15px 0,calc(100% - 15px) 0,100% 100%,0 100%)}
</style>
</head>
<body>

<svg width="0" height="0" style="position:absolute" aria-hidden="true">
  <defs>
    <symbol id="i-phone" viewBox="0 0 10 10"><path d="M2 1l2 2-1 1.5c.6 1.2 1.3 1.9 2.5 2.5L7 6l2 2-1.5 1.5C4.5 9 1 5.5.5 2.5z"/></symbol>
    <symbol id="i-fax" viewBox="0 0 10 10"><rect x="1" y="4" width="8" height="5"/><rect x="3" y="1" width="4" height="3"/><path d="M3 6.5h4"/></symbol>
    <symbol id="i-mail" viewBox="0 0 10 10"><rect x="1" y="2.5" width="8" height="5.5"/><path d="M1 2.5l4 3 4-3"/></symbol>
    <symbol id="i-web" viewBox="0 0 10 10"><circle cx="5" cy="5" r="4"/><ellipse cx="5" cy="5" rx="1.7" ry="4"/><path d="M1 5h8"/></symbol>
  </defs>
</svg>

<section class="sheet envelope">
  <div class="brand"><span class="mark"></span><span class="name">Energieberatung<small>MIRA WENDEL</small></span></div>
</section>

<section class="sheet card-front">
  <div class="brand"><span class="mark"></span><span class="name">Energieberatung<small>MIRA WENDEL</small></span></div>
  <p class="role"><b>Mira Wendel</b> - Geschäftsleitung</p>
  <p class="address small">Musterstraße 126<br>00000 Musterstadt</p>
  <ul class="contact">
    <li><svg><use href="#i-phone"/></svg>+49 1234-56789-0</li>
    <li><svg><use href="#i-fax"/></svg>+49 1234-56789-1</li>
    <li><svg><use href="#i-mail"/></svg>info@beispielhaus.de</li>
    <li><svg><use href="#i-web"/></svg>www.beispielhaus.de</li>
  </ul>
  <div class="band"></div>
</section>

<section class="sheet card-back">
  <div class="brand"><span class="mark"></span><span class="name">Mira Wendel</span></div>
  <p class="url">www.beispielhaus.de</p>
</section>

<section class="sheet card-grey">
  <div class="brand"><span class="mark"></span><span class="name">Energieberatung<small>MIRA WENDEL</small></span></div>
</section>

<section class="sheet card-mono">
  <div class="brand"><span class="mark"></span><span class="name">Energieberatung<small>MIRA WENDEL</small></span></div>
</section>

<section class="sheet letterhead">
  <div class="band-top"></div>
  <div class="brand"><span class="mark"></span><span class="name">Energieberatung<small>MIRA WENDEL</small></span></div>
  <ul class="contact">
    <li><svg><use href="#i-phone"/></svg>+49 1234-56789-0</li>
    <li><svg><use href="#i-fax"/></svg>+49 1234-56789-1</li>
    <li><svg><use href="#i-mail"/></svg>info@beispielhaus.de</li>
    <li><svg><use href="#i-web"/></svg>www.beispielhaus.de</li>
  </ul>
  <p class="sender">Energieberatung Mira Wendel - Postfach 0000 - 00000 Musterstadt</p>

  <footer class="footer">
    <div class="col"><b>Energieberatung Mira Wendel</b>Musterstraße 126<br>00000 Musterstadt</div>
    <div class="col"><b>Geschäftsführer</b>Mira Wendel<br>Energieberaterin</div>
    <div class="col">
      <ul class="contact">
        <li><svg><use href="#i-phone"/></svg>+49 1234-56789-0</li>
        <li><svg><use href="#i-fax"/></svg>+49 1234-56789-1</li>
        <li><svg><use href="#i-web"/></svg>www.beispielhaus.de</li>
      </ul>
    </div>
    <div class="col"><b>Amtsgericht Stadt</b>ABC 0000XX<br>UST-ID DE 000XX</div>
    <div class="col"><b>Bankverbindung ABC</b>IBAN DE12 3456 7890 1234 5678<br>BIC ABCDEF12345</div>
  </footer>
  <div class="band-bottom"></div>
</section>

</body>
</html>
```